Redesign cement bags for leading cement producer in south east asia

We are from Larkfield cement and would like to redesign our bag to relaunch the product line. Our bags are made of high quality PP woven sack. We are one of the leading cement producers and we want our bags to have a Larkfield classy look on each visible side when it is loading in a truck or stacking on a pallet.

Thank you for interesting in this project. Good luck.

Project Deadline Extended Reason: Hi all, I have received requests to extend the deadline. Some of the work requires revising and some of them are still on process. To be fair, I also raise my budget to compensate the time. Thanks all for your participation. Added Sunday, July 10, 2016

Target Market(s)

Construction

Industry/Entity Type

Cement

Requirements
Must have
• You will have to design two bags for two cement grades. 52.5 is of higher grade and 42.5 is of lower grade. Both are similar in design but a distinctive colours to differentiate the two at once. Please look at Reference picture 2 for ideas.
Nice to have
• You do not have to change the original logo but the Larkfield cement word font changes are required. There are no restrictions to colours and font but please refrain from using feminine colours. Instructions on rear side of the bags are now included in the scope. Please create new layout and design new user friendly symbols.
Should not have
• Since cement is a dusty product, you need avoid some colours like black as background. The dust need to be less obvious to attract attention. Our previous base colour are shown in below.
• We want a fresh look on our bag, please do not just copy our old design and make small changes. I have attached our competitors' design, please refrain from using their design as well.
• It is recommend to do some research on cement bag sector.

```html
<!DOCTYPE html>
<html lang="en">
<head>
<meta charset="utf-8">
<title>Larkfield Cement – Bag Range</title>
<link href="https://fonts.googleapis.com/css2?family=Montserrat:wght@700;800;900&display=swap" rel="stylesheet">
<style>
  :root {
    --backdrop: #c9c9c9;
    --grade-high: #d01719;
    --grade-standard: #1d56a0;
    --sack-white: #f2f2f2;
    --sack-shade: #dcdcdc;
    --ink: #0a0a0a;
    --paper: #ffffff;
  }
  html, body {
    margin: 0;
    padding: 0;
    width: 1200px;
    height: 1200px;
    overflow: hidden;
    background: var(--backdrop);
    font-family: "Montserrat", Arial, sans-serif;
  }
  .range {
    position: relative;
    width: 1200px;
    height: 1200px;
  }
  .bag {
    position: absolute;
    top: 238px;
    width: 480px;
    height: 745px;
  }
  .bag--high { left: 108px; --grade: var(--grade-high); }
  .bag--standard { left: 632px; --grade: var(--grade-standard); }
  .bag svg { display: block; width: 100%; height: 100%; }
  .bag__field { fill: var(--grade); }
  .bag__swoosh { fill: url(#sackShade); }
  .bag__seal { fill: var(--grade); stroke: var(--paper); stroke-width: 4; }
  .brand-name { font-weight: 900; font-size: 52px; fill: var(--paper); letter-spacing: -1px; }
  .brand-tagline { font-weight: 800; font-size: 15.5px; fill: var(--paper); letter-spacing: 0.6px; }
  .product-name { font-weight: 900; font-size: 38px; fill: var(--ink); letter-spacing: -0.5px; }
  .class-label { font-weight: 800; font-size: 13px; fill: var(--ink); }
  .class-standard { font-weight: 800; font-size: 15px; fill: var(--ink); }
  .class-grade { font-weight: 900; font-size: 58px; fill: var(--ink); letter-spacing: -1px; }
  .origin { font-weight: 800; font-size: 14px; fill: var(--ink); }
  .weight-label { font-weight: 800; font-size: 7px; fill: var(--paper); }
  .weight-value { font-weight: 900; font-size: 32px; fill: var(--paper); letter-spacing: -0.5px; }
</style>
</head>
<body>
<main class="range">
  <svg width="0" height="0" style="position:absolute" aria-hidden="true">
    <defs>
      <linearGradient id="sackShade" x1="0" y1="0" x2="1" y2="1">
        <stop offset="0" stop-color="#f6f6f6"/>
        <stop offset="1" stop-color="#dedede"/>
      </linearGradient>
    </defs>
  </svg>

  <section class="bag bag--high" aria-label="Larkfield Portland cement, strength class 52.5">
    <svg viewBox="0 0 480 745">
      <rect class="bag__field" width="480" height="745"/>
      <path class="bag__swoosh" d="M480,112 C380,150 200,260 150,390 C100,520 110,660 160,745 L480,745 Z"/>
      <circle class="bag__seal" cx="228" cy="315" r="138"/>
      <text class="brand-name" x="218" y="103" text-anchor="middle">LARKFIELD</text>
      <text class="brand-tagline" x="226" y="130" text-anchor="middle">EXPORT QUALITY CEMENT</text>
      <text class="product-name" x="318" y="502" text-anchor="middle">PORTLAND</text>
      <text class="product-name" x="310" y="547" text-anchor="middle">CEMENT</text>
      <text class="class-label" x="240" y="595">STRENGTH CLASS</text>
      <text class="class-standard" x="240" y="611">EN 197-1 (2000)</text>
      <text class="class-grade" x="306" y="668" text-anchor="middle">52.5</text>
      <text class="origin" x="310" y="712" text-anchor="middle">PRODUCT OF MYANMAR</text>
      <text class="weight-label" x="20" y="663">NET WEIGHT</text>
      <text class="weight-value" x="18" y="695">50kg</text>
    </svg>
  </section>

  <section class="bag bag--standard" aria-label="Larkfield Portland cement, strength class 42.5">
    <svg viewBox="0 0 480 745">
      <rect class="bag__field" width="480" height="745"/>
      <path class="bag__swoosh" d="M480,112 C380,150 200,260 150,390 C100,520 110,660 160,745 L480,745 Z"/>
      <circle class="bag__seal" cx="228" cy="315" r="138"/>
      <text class="brand-name" x="218" y="103" text-anchor="middle">LARKFIELD</text>
      <text class="brand-tagline" x="226" y="130" text-anchor="middle">EXPORT QUALITY CEMENT</text>
      <text class="product-name" x="318" y="502" text-anchor="middle">PORTLAND</text>
      <text class="product-name" x="310" y="547" text-anchor="middle">CEMENT</text>
      <text class="class-label" x="240" y="595">STRENGTH CLASS</text>
      <text class="class-standard" x="240" y="611">EN 197-1 (2000)</text>
      <text class="class-grade" x="306" y="668" text-anchor="middle">42.5</text>
      <text class="origin" x="310" y="712" text-anchor="middle">PRODUCT OF MYANMAR</text>
      <text class="weight-label" x="20" y="663">NET WEIGHT</text>
      <text class="weight-value" x="18" y="695">50kg</text>
    </svg>
  </section>
</main>
</body>
</html>
```